The Wellness Barn Business Card

Info for the front..... (in whichever order and layout looks best)
Carla Penhallow
Physiotherapist
4/37 Upper Creekbank Rd
Tallowbrook
QLD 4712
0462305178
carlapenhallow57@mailbox.example
www.thewellnessbarn.example.au
on the back I would like to be able to write appointments so probably just that heading with lines.
I like a sort of rustic style but mostly professional, colours in naturals, beige, brown, green etc. I dont mind if the logo colour is changed slightly to suit.

```html
<!DOCTYPE html>
<html lang="en">
<head>
<meta charset="utf-8">
<title>The Wellness Barn Business Card</title>
<link rel="stylesheet" href="https://fonts.googleapis.com/css2?family=Lato:wght@400;700;900&family=Montserrat:wght@500;700&display=swap">
<style>
  :root {
    --bg: #2a2a2a;
    --green: #2d4a1f;
    --green-ink: #27421a;
    --brown: #4a3420;
    --paper: #f2f2ee;
    --white: #ffffff;
    --muted: #6f7d66;
  }
  * { margin: 0; padding: 0; box-sizing: border-box; }
  html, body { width: 1200px; height: 875px; overflow: hidden; background: var(--bg); }
  .canvas { position: relative; width: 1200px; height: 875px; background: var(--bg); }

  .card { position: absolute; width: 540px; height: 310px; border-radius: 18px; overflow: hidden; }

  /* Back: appointment card */
  .card-back { left: 50px; top: 150px; background: var(--paper); color: var(--green-ink); font-family: "Montserrat", sans-serif; }
  .appt-title { position: absolute; top: 40px; width: 100%; text-align: center; font-weight: 700; font-size: 28px; letter-spacing: 0.5px; }
  .appt-line { position: absolute; left: 50px; right: 50px; display: flex; align-items: flex-end; font-size: 14px; font-weight: 500; letter-spacing: 0.5px; }
  .appt-line .fill { flex: 1; border-bottom: 1.5px dotted var(--green-ink); margin: 0 6px 4px; }
  .line-name { top: 100px; }
  .line-date { top: 140px; }
  .days { position: absolute; top: 185px; left: 50px; right: 50px; display: flex; justify-content: space-between; font-size: 13px; font-weight: 500; }
  .day { display: flex; align-items: center; gap: 5px; }
  .box { width: 13px; height: 13px; border: 1.5px solid var(--green-ink); }
  .appt-note { position: absolute; top: 240px; left: 60px; right: 60px; text-align: center; font-family: "Lato", sans-serif; font-size: 12px; line-height: 1.4; }

  /* Front: contact card */
  .card-front { left: 610px; top: 415px; background: var(--green); font-family: "Lato", sans-serif; color: var(--white); }
  .front-shape { position: absolute; inset: 0; }
  .brand-name { position: absolute; top: 62px; right: 30px; width: 170px; text-align: center; color: var(--green); font-weight: 900; font-size: 30px; line-height: 1.05; }
  .person { position: absolute; left: 32px; top: 118px; }
  .person-name { font-weight: 700; font-size: 24px; letter-spacing: 1px; text-transform: uppercase; }
  .person-role { font-size: 15px; margin-top: 2px; }
  .contacts { position: absolute; left: 32px; top: 185px; font-size: 13px; line-height: 1.35; }
  .contact { display: flex; gap: 8px; margin-bottom: 4px; }
  .contact svg { flex: none; width: 13px; height: 13px; margin-top: 2px; }
  .contact strong { font-weight: 700; }
</style>
</head>
<body>
<main class="canvas">

  <section class="card card-back" aria-label="Appointment side">
    <h2 class="appt-title">NEXT APPOINTMENT</h2>
    <div class="appt-line line-name"><span>NAME</span><span class="fill"></span></div>
    <div class="appt-line line-date"><span>DATE</span><span class="fill"></span><span>TIME</span><span class="fill"></span><span>AM/PM</span></div>
    <div class="days">
      <span class="day"><span class="box"></span>MON</span>
      <span class="day"><span class="box"></span>TUES</span>
      <span class="day"><span class="box"></span>WED</span>
      <span class="day"><span class="box"></span>THU</span>
      <span class="day"><span class="box"></span>FRI</span>
      <span class="day"><span class="box"></span>SAT</span>
    </div>
    <p class="appt-note">If you are unable to keep your appointment, please call us to reschedule at least 48 hours prior to your appointment.</p>
  </section>

  <section class="card card-front" aria-label="Contact side">
    <svg class="front-shape" viewBox="0 0 540 310" preserveAspectRatio="none" aria-hidden="true">
      <path d="M318 0 Q338 230 540 292" fill="none" stroke="var(--brown)" stroke-width="6"/>
      <path d="M308 0 Q330 236 540 300" fill="none" stroke="var(--white)" stroke-width="3"/>
      <path d="M325 0 Q345 222 540 284 L540 0 Z" fill="var(--white)"/>
    </svg>
    <div class="brand-name">The Wellness Barn</div>
    <div class="person">
      <h1 class="person-name">Carla Penhallow</h1>
      <p class="person-role">Physiotherapist</p>
    </div>
    <div class="contacts">
      <div class="contact">
        <svg viewBox="0 0 12 12"><path d="M6 0.5a4 4 0 0 1 4 4c0 3-4 7-4 7s-4-4-4-7a4 4 0 0 1 4-4z" fill="var(--white)"/><circle cx="6" cy="4.5" r="1.5" fill="var(--green)"/></svg>
        <span><strong>The Wellness Barn</strong><br>4/37 Upper Creekbank Rd<br>Tallowbrook, QLD 4712</span>
      </div>
      <div class="contact">
        <svg viewBox="0 0 12 12"><path d="M2.5 1l2 0.5 0.8 2.5-1.4 1a6 6 0 0 0 3 3l1-1.4 2.5 0.8 0.5 2c-5 1.5-10-3.5-8.9-8.4z" fill="var(--white)"/></svg>
        <span>0462305178</span>
      </div>
      <div class="contact">
        <svg viewBox="0 0 12 12"><rect x="0.5" y="2" width="11" height="8" fill="var(--white)"/><path d="M0.5 2l5.5 4.5 5.5-4.5" fill="none" stroke="var(--green)" stroke-width="1"/></svg>
        <span>carlapenhallow57@mailbox.example</span>
      </div>
      <div class="contact">
        <svg viewBox="0 0 12 12"><circle cx="6" cy="6" r="5.5" fill="var(--white)"/><path d="M0.5 6h11M6 0.5c-2.5 3-2.5 8 0 11M6 0.5c2.5 3 2.5 8 0 11" fill="none" stroke="var(--green)" stroke-width="0.9"/></svg>
        <span>www.thewellnessbarn.example.au</span>
      </div>
    </div>
  </section>

</main>
</body>
</html>
```